Mobile Dental Clinic Signage

We have a company called Coastline roving dental care.

We have 5 trucks and need the outsides of the truck designed.

Colours we like used is a sea blue, dark blue, light blue basically all the blue colours as well as grey and white. We do not like too simple but something bright and professional.

We will need the following put on the truck
- Mobile Dental Centre
- Our logo
- Contact number 1300TEETHY
- website www.crdc.net.au
- all social media symbols
- Somewhere on the truck have sections where is says
servicing aged care facilities, schools, corporations and aboriginal communities.

I have attached our current signage on the mobile clinic but we need this revamped. I have also attached a previous graphic designer work to give a idea although we where not that impressed with the designs

We like the swirf look but maybe in different colours. Hope all this makes sense. And if the design can cover the windows that would be great.

Industry/Entity Type

Dental

```html
<!DOCTYPE html>
<html lang="en">
<head>
<meta charset="utf-8">
<title>Mobile Dental Centre – Truck Signage</title>
<link rel="stylesheet" href="https://fonts.googleapis.com/css2?family=Lobster&family=Montserrat:wght@500;600&display=swap">
<style>
  :root{
    --page:#ffffff;
    --panel-top:#eef4f6;
    --panel-bottom:#dde9ee;
    --ink-purple:#3b2a62;
    --band-purple:#3d2b66;
    --band-purple-deep:#2f2152;
    --sea-blue:#3a8fd0;
    --light-blue:#7cc3e8;
    --list-ink:#4b3a7a;
    --white:#ffffff;
    --photo-light:#e9d3cc;
    --photo-mid:#c99a8e;
    --photo-shade:#9fb8c6;
  }
  *{margin:0;padding:0;box-sizing:border-box}
  html,body{width:1200px;height:697px;overflow:hidden;background:var(--page)}
  body{position:relative;font-family:"Montserrat",Arial,sans-serif}

  .truck-banner{
    position:absolute;width:1060px;height:208px;overflow:hidden;
    background:linear-gradient(180deg,var(--panel-top),var(--panel-bottom));
  }
  .truck-banner--driver{left:70px;top:82px}
  .truck-banner--kerb{left:63px;top:398px}

  .swirl{position:absolute;left:0;top:0;width:1060px;height:208px}
  .truck-banner--kerb .swirl{transform:scaleX(-1)}

  .smile-photo{position:absolute;top:0;width:250px;height:185px}
  .truck-banner--driver .smile-photo{left:0}
  .truck-banner--kerb .smile-photo{right:0;transform:scaleX(-1)}

  .title{
    position:absolute;font-family:"Lobster",cursive;font-size:54px;line-height:1;
    color:var(--ink-purple);white-space:nowrap;transform:translateX(-50%);
  }
  .truck-banner--driver .title{left:500px;top:10px}
  .truck-banner--kerb .title{left:530px;top:12px}

  .service-pill{
    position:absolute;height:29px;padding:0 14px;border-radius:15px;
    background:var(--sea-blue);color:var(--white);font-weight:600;font-size:19px;
    line-height:29px;letter-spacing:.3px;white-space:nowrap;
  }
  .truck-banner--driver .service-pill{left:270px;top:86px}
  .truck-banner--kerb .service-pill{left:502px;top:96px}

  .service-list{position:absolute;list-style:none;font-weight:500;font-size:17px;line-height:20px;color:var(--list-ink);white-space:nowrap}
  .service-list li{display:flex;align-items:center;gap:6px}
  .chev{width:8px;height:10px;flex:none}
  .truck-banner--driver .list-a{left:220px;top:126px}
  .truck-banner--driver .list-b{left:330px;top:126px}
  .truck-banner--kerb .service-list{text-align:right}
  .truck-banner--kerb .service-list li{justify-content:flex-end}
  .truck-banner--kerb .list-a{right:264px;top:132px}
  .truck-banner--kerb .list-b{right:160px;top:134px}

  .brand-box{
    position:absolute;width:201px;height:60px;background:var(--white);border-radius:4px;
    display:flex;align-items:center;justify-content:center;gap:8px;padding:0 10px;
  }
  .brand-box .dot{width:12px;height:12px;border-radius:50%;background:var(--sea-blue);flex:none}
  .brand-name{font-size:13px;font-weight:600;color:var(--ink-purple);line-height:1.2}
  .truck-banner--driver .brand-box{left:815px;top:19px}
  .truck-banner--kerb .brand-box{left:51px;top:19px}

  .social{position:absolute;display:flex;align-items:center;gap:8px;font-size:18px;font-weight:500;color:var(--ink-purple);white-space:nowrap}
  .social .chev{margin:0 4px}
  .social-tile{width:25px;height:25px;border-radius:5px;background:var(--ink-purple)}
  .truck-banner--driver .social{left:690px;top:109px}
  .truck-banner--kerb .social{left:76px;top:104px}

  .contact{position:absolute;display:flex;align-items:center;gap:8px;font-size:19px;font-weight:500;color:var(--white);white-space:nowrap}
  .contact svg{flex:none}
  .truck-banner--driver .contact-phone{left:628px;top:174px}
  .truck-banner--driver .contact-web{left:808px;top:174px}
  .truck-banner--kerb .contact-web{left:38px;top:176px}
  .truck-banner--kerb .contact-phone{left:272px;top:176px}
</style>
</head>
<body>

<!-- Driver side -->
<section class="truck-banner truck-banner--driver" aria-label="Driver side panel">
  <svg class="swirl" viewBox="0 0 1060 208" aria-hidden="true">
    <path d="M0 160 C260 188 560 132 1060 140 L1060 152 C560 144 260 200 0 174 Z" fill="var(--light-blue)"/>
    <path d="M0 172 C260 200 560 146 1060 152 L1060 208 L0 208 Z" fill="var(--band-purple)"/>
    <path d="M0 196 C300 208 600 170 1060 176 L1060 208 L0 208 Z" fill="var(--band-purple-deep)" opacity=".5"/>
  </svg>
  <svg class="smile-photo" viewBox="0 0 250 185" role="img" aria-label="Photo of a smiling woman during a dental check-up">
    <defs><linearGradient id="photoA" x1="0" y1="0" x2="1" y2="1">
      <stop offset="0" stop-color="var(--photo-shade)"/><stop offset=".45" stop-color="var(--photo-light)"/><stop offset="1" stop-color="var(--photo-mid)"/></linearGradient></defs>
    <path d="M0 0 H240 C250 60 230 140 160 185 H0 Z" fill="url(#photoA)"/>
  </svg>

  <h1 class="title">Mobile Dental Centre</h1>
  <div class="service-pill">SERVICING AGED CARE :</div>
  <ul class="service-list list-a">
    <li><svg class="chev" viewBox="0 0 8 10"><path d="M1 0 L7 5 L1 10 L3 5Z" fill="var(--sea-blue)"/></svg>Facilities</li>
    <li><svg class="chev" viewBox="0 0 8 10"><path d="M1 0 L7 5 L1 10 L3 5Z" fill="var(--sea-blue)"/></svg>Schools</li>
  </ul>
  <ul class="service-list list-b">
    <li><svg class="chev" viewBox="0 0 8 10"><path d="M1 0 L7 5 L1 10 L3 5Z" fill="var(--sea-blue)"/></svg>Corporations</li>
    <li><svg class="chev" viewBox="0 0 8 10"><path d="M1 0 L7 5 L1 10 L3 5Z" fill="var(--sea-blue)"/></svg>Aboriginal Communities</li>
  </ul>

  <div class="brand-box"><span class="dot"></span><span class="brand-name">Coastline roving dental care</span></div>

  <div class="social">find us on
    <svg class="chev" viewBox="0 0 8 10"><path d="M1 0 L7 5 L1 10 L3 5Z" fill="var(--sea-blue)"/></svg>
    <span class="social-tile"></span><span class="social-tile"></span><span class="social-tile"></span><span class="social-tile"></span><span class="social-tile"></span>
  </div>

  <div class="contact contact-phone">
    <svg width="12" height="20" viewBox="0 0 12 20"><rect x="1" y="1" width="10" height="18" rx="2" fill="none" stroke="var(--white)" stroke-width="1.6"/><rect x="3" y="4" width="6" height="9" fill="var(--white)"/></svg>1300TEETHY
  </div>
  <div class="contact contact-web">
    <svg width="20" height="20" viewBox="0 0 20 20" fill="none" stroke="var(--white)" stroke-width="1.5"><circle cx="10" cy="10" r="8.5"/><ellipse cx="10" cy="10" rx="3.8" ry="8.5"/><path d="M1.5 10h17M3 5.5h14M3 14.5h14"/></svg>www.crdc.net.au
  </div>
</section>

<!-- Kerb side -->
<section class="truck-banner truck-banner--kerb" aria-label="Kerb side panel">
  <svg class="swirl" viewBox="0 0 1060 208" aria-hidden="true">
    <path d="M0 160 C260 188 560 132 1060 140 L1060 152 C560 144 260 200 0 174 Z" fill="var(--light-blue)"/>
    <path d="M0 172 C260 200 560 146 1060 152 L1060 208 L0 208 Z" fill="var(--band-purple)"/>
    <path d="M0 196 C300 208 600 170 1060 176 L1060 208 L0 208 Z" fill="var(--band-purple-deep)" opacity=".5"/>
  </svg>
  <svg class="smile-photo" viewBox="0 0 250 185" role="img" aria-label="Photo of a smiling woman during a dental check-up">
    <defs><linearGradient id="photoB" x1="0" y1="0" x2="1" y2="1">
      <stop offset="0" stop-color="var(--photo-shade)"/><stop offset=".45" stop-color="var(--photo-light)"/><stop offset="1" stop-color="var(--photo-mid)"/></linearGradient></defs>
    <path d="M0 0 H240 C250 60 230 140 160 185 H0 Z" fill="url(#photoB)"/>
  </svg>

  <div class="brand-box"><span class="dot"></span><span class="brand-name">Coastline roving dental care</span></div>
  <h2 class="title">Mobile Dental Centre</h2>

  <div class="social">
    <span class="social-tile"></span><span class="social-tile"></span><span class="social-tile"></span><span class="social-tile"></span><span class="social-tile"></span>
    <svg class="chev" viewBox="0 0 8 10"><path d="M7 0 L1 5 L7 10 L5 5Z" fill="var(--sea-blue)"/></svg>find us on
  </div>

  <div class="service-pill">SERVICING AGED CARE :</div>
  <ul class="service-list list-a">
    <li>Corporations<svg class="chev" viewBox="0 0 8 10"><path d="M7 0 L1 5 L7 10 L5 5Z" fill="var(--sea-blue)"/></svg></li>
    <li>Aboriginal Communities<svg class="chev" viewBox="0 0 8 10"><path d="M7 0 L1 5 L7 10 L5 5Z" fill="var(--sea-blue)"/></svg></li>
  </ul>
  <ul class="service-list list-b">
    <li>Facilities<svg class="chev" viewBox="0 0 8 10"><path d="M7 0 L1 5 L7 10 L5 5Z" fill="var(--sea-blue)"/></svg></li>
    <li>Schools<svg class="chev" viewBox="0 0 8 10"><path d="M7 0 L1 5 L7 10 L5 5Z" fill="var(--sea-blue)"/></svg></li>
  </ul>

  <div class="contact contact-web">www.crdc.net.au
    <svg width="20" height="20" viewBox="0 0 20 20" fill="none" stroke="var(--white)" stroke-width="1.5"><circle cx="10" cy="10" r="8.5"/><ellipse cx="10" cy="10" rx="3.8" ry="8.5"/><path d="M1.5 10h17M3 5.5h14M3 14.5h14"/></svg>
  </div>
  <div class="contact contact-phone">1300TEETHY
    <svg width="12" height="20" viewBox="0 0 12 20"><rect x="1" y="1" width="10" height="18" rx="2" fill="none" stroke="var(--white)" stroke-width="1.6"/><rect x="3" y="4" width="6" height="9" fill="var(--white)"/></svg>
  </div>
</section>

</body>
</html>
```